Upscale and cool gun range / bar + lounge. Think axe throwing, but much cooler.

capture interest and make them want to know more.

s/b more on the cool and hip side to be on brand

will be offering a gift card. example attached

```html
<!DOCTYPE html>
<html lang="en">
<head>
<meta charset="utf-8">
<title>Farsight – Gift Card Fold Layout</title>
<link rel="stylesheet" href="https://fonts.googleapis.com/css2?family=Poppins:ital,wght@0,300;0,400;0,600;0,700;0,900;1,800&display=swap">
<style>
  :root {
    --card-black: #1c1c1c;
    --ink: #1a1a1a;
    --paper: #ffffff;
    --signal-orange: #ffa400;
    --stamp-deep: #e89400;
    --white: #ffffff;
  }
  * { margin: 0; padding: 0; box-sizing: border-box; }
  html, body {
    width: 1049px; height: 1200px; overflow: hidden;
    background: var(--paper);
    font-family: "Poppins", sans-serif;
  }
  .sheet { position: relative; width: 1049px; height: 1200px; }

  .view-label {
    position: absolute; width: 380px; text-align: center;
    font-weight: 300; font-size: 17px; letter-spacing: 3px; color: var(--ink);
  }
  .view-label--closed { left: 58px; top: 12px; }
  .view-label--opened { left: 607px; top: 12px; }
  .view-label--cover { left: 58px; top: 1146px; }

  .fold-note {
    position: absolute; left: 459px; top: 236px; width: 120px;
    text-align: center; font-weight: 300; font-size: 16px; line-height: 21px;
    letter-spacing: 2px; color: var(--ink);
  }

  .card-front {
    position: absolute; left: 58px; top: 48px; width: 384px; height: 594px;
    background: var(--card-black);
  }
  .cover-cutout { position: absolute; left: 58px; top: 693px; width: 384px; height: 456px; }
  .cover-cutout svg { position: absolute; inset: 0; }

  .brand-mark { position: absolute; left: 0; width: 384px; text-align: center; }
  .brand-mark__dot {
    display: block; margin: 0 auto; width: 40px; height: 40px;
    border: 1.5px solid var(--white); border-radius: 50%;
  }
  .brand-mark__name {
    display: block; margin-top: 12px; color: var(--white);
    font-weight: 600; font-size: 10px; letter-spacing: 3.5px; padding-left: 3.5px;
  }

  .stamp-art {
    position: absolute; left: 62px; width: 260px; height: 260px; border-radius: 50%;
    background: radial-gradient(circle, var(--signal-orange) 0%, var(--stamp-deep) 100%);
  }

  .risk-note {
    position: absolute; left: 0; width: 384px; text-align: center;
    color: var(--white); font-weight: 400; font-size: 11.5px; letter-spacing: 2px;
  }

  .card-open { position: absolute; left: 607px; top: 48px; width: 384px; height: 1050px; }
  .flow-arrow { position: absolute; left: 0; top: 0; }
</style>
</head>
<body>
<main class="sheet">

  <p class="view-label view-label--closed">CLOSED VIEW (A)</p>
  <p class="view-label view-label--opened">OPENED VIEW (B)</p>

  <section class="card-front" aria-label="Closed card front">
    <div class="brand-mark" style="top:42px">
      <span class="brand-mark__dot"></span>
      <span class="brand-mark__name">FARSIGHT</span>
    </div>
    <div class="stamp-art" style="top:182px" role="img" aria-label="Orange rubber stamp reading Top Secret, Confidential"></div>
    <p class="risk-note" style="top:563px">OPEN AT YOUR OWN RISK</p>
  </section>

  <p class="fold-note">“A”<br>BECOMES<br>“B” WHEN<br>OPENED<br>DOWNARDS</p>

  <svg class="flow-arrow" width="1049" height="1200" aria-hidden="true">
    <g fill="none" stroke="var(--ink)" stroke-width="5" stroke-linecap="round" stroke-linejoin="round">
      <path d="M470 386 Q518 382 568 387"/>
      <path d="M550 372 L570 387 L551 398"/>
      <path d="M665 1052 Q595 1105 482 1099"/>
      <path d="M514 1079 L480 1099 L516 1122"/>
    </g>
  </svg>

  <svg class="card-open" viewBox="0 0 384 1050" aria-label="Opened card inside">
    <path d="M0 0 H384 V995 L322 983 A145 145 0 0 1 61 933 L0 922 Z" fill="var(--card-black)"/>
    <circle cx="192" cy="62" r="20" fill="none" stroke="var(--white)" stroke-width="1.5"/>
    <text x="193.75" y="105" text-anchor="middle" fill="var(--white)" font-family="Poppins, sans-serif" font-weight="600" font-size="10" letter-spacing="3.5">FARSIGHT</text>

    <g class="headline" font-family="Poppins, sans-serif">
      <text x="20" y="242" font-weight="900" font-size="88" fill="var(--white)" textLength="341" lengthAdjust="spacingAndGlyphs">LOOK’N</text>
      <text x="15" y="286" font-weight="300" font-size="46" fill="var(--white)" textLength="349" lengthAdjust="spacingAndGlyphs">SOMEWHERE TO</text>
      <text x="13" y="365" font-weight="900" font-size="100" fill="var(--white)" textLength="347" lengthAdjust="spacingAndGlyphs">SHOOT</text>
      <text x="17" y="438" font-weight="900" font-size="92" fill="var(--signal-orange)" textLength="246" lengthAdjust="spacingAndGlyphs">GUNS</text>
      <text x="284" y="475" font-weight="300" font-size="98" fill="var(--white)" textLength="70" lengthAdjust="spacingAndGlyphs">&amp;</text>
      <text x="19" y="500" font-weight="900" font-size="72" fill="var(--white)" textLength="247" lengthAdjust="spacingAndGlyphs">SHOOT</text>
      <text x="21" y="582" font-weight="900" font-size="104" fill="var(--signal-orange)" textLength="337" lengthAdjust="spacingAndGlyphs">BEERS?</text>
    </g>

    <text x="193" y="653" text-anchor="middle" font-family="Poppins, sans-serif" font-style="italic" font-weight="800" font-size="21" fill="var(--white)" textLength="253" lengthAdjust="spacingAndGlyphs">WE GOT YA COVERED!</text>

    <g class="contact" font-family="Poppins, sans-serif" fill="var(--white)">
      <text x="26" y="731" font-weight="600" font-size="18">Contact us at:</text>
      <path d="M46 740 q-3 4 0 9 q3 4 6 2 l-1.5 -2.5 q-1.5 1 -2.5 -1 q-1 -2 0 -3.5 l1.5 1 l1 -2.5 z" fill="var(--white)"/>
      <text x="61" y="752" font-weight="300" font-size="18">905-555-0148</text>
      <rect x="42" y="764" width="11" height="8" fill="none" stroke="var(--white)" stroke-width="1.2"/>
      <path d="M42 764 L47.5 769 L53 764" fill="none" stroke="var(--white)" stroke-width="1.2"/>
      <text x="61" y="773" font-weight="300" font-size="18">info@farsight.ca</text>
      <text x="26" y="801" font-weight="600" font-size="18">Or visit us at:</text>
      <path d="M47 817 c-3 -4 -5 -6 -5 -8.5 a5 5 0 0 1 10 0 c0 2.5 -2 4.5 -5 8.5 z" fill="none" stroke="var(--white)" stroke-width="1.3"/>
      <circle cx="47" cy="808.5" r="1.5" fill="var(--white)"/>
      <text x="61" y="822" font-weight="300" font-size="18">88 Marlow Road, Unit 2B</text>
      <text x="61" y="843" font-weight="700" font-size="18">City of ASHBURY</text>
      <text x="193" y="898" text-anchor="middle" font-weight="300" font-size="18" textLength="260" lengthAdjust="spacing">https://www.farsight.ca</text>
    </g>
  </svg>

  <section class="cover-cutout" aria-label="Cover cut-out">
    <svg width="384" height="456" viewBox="0 0 384 456" aria-hidden="true">
      <path d="M0 456 V122 L35 114 A164 164 0 0 1 321 59 L384 48 V456 Z" fill="var(--card-black)"/>
    </svg>
    <div class="stamp-art" style="top:37px" role="img" aria-label="Orange rubber stamp reading Top Secret, Confidential"></div>
    <p class="risk-note" style="top:425px">OPEN AT YOUR OWN RISK</p>
  </section>

  <p class="view-label view-label--cover">COVER CUT-OUT</p>

</main>
</body>
</html>
```